依頼詳細
アパートのオーナー様が問合せをしたくなるデザインで
シンプルで、誠実感のあるデザイン。
記載項目
カナメリビング株式会社 岐阜県関市桜台3丁目4-27
スミカネットFC岐阜北店、スミカネットFC各務原21号店、スミカネットFC関店経営。
電話番号0575-38-4716
×
東和住まいリンク株式会社
全国で社宅代行を受託
社宅として、一括借上
サイズ
A4
ページ数
片面
希望イメージ
シンプル 複雑
単色 カラフル
暗い 明るい
日常 高級
遊び心 厳粛
未来的 伝統的
女性的 男性的
希望する色
赤系、青系
納品ファイル
補足説明
添付は会社のいままで作成したチラシ
参考にはしなくてもいいです。
会社の情報のみ参考
■ 選んだ理由

シンプルですが、買取・管理の区別がはっきりしていて分かりやすい。
色合いも、きれいです。

■ 提案者全員のお礼・コメント

この度は、お時間を割いて多数の応募ありがとうございます。
皆様のご提案はそれぞれの良さがあり、大変悩みました。
私の分かりにくい説明でも、ここまで仕上げるのは見事です。
また、機会がありましたら是非お願い致します。

```html
<!DOCTYPE html>
<html lang="ja">
<head>
<meta charset="utf-8">
<title>アパート・マンション買取のご案内</title>
<link href="https://fonts.googleapis.com/css2?family=Noto+Sans+JP:wght@400;500;700;900&display=swap" rel="stylesheet">
<style>
:root{
  --navy:#1d3573;
  --blue:#2c6cb4;
  --blue-light:#e7f0fa;
  --red:#d3262c;
  --yellow:#f6e24c;
  --gray:#555;
  --ink:#222;
  --white:#fff;
}
*{margin:0;padding:0;box-sizing:border-box}
html,body{width:846px;height:1200px;overflow:hidden;background:var(--white)}
body{font-family:"Noto Sans JP",sans-serif;color:var(--ink);position:relative}
.headline{position:absolute;left:0;right:0;top:18px;text-align:center;color:var(--navy);font-weight:900;font-size:40px;line-height:1.3;letter-spacing:1px}
.subline{position:absolute;left:0;right:0;top:178px;text-align:center;color:var(--gray);font-size:19px;font-weight:500}
.photo{position:absolute;left:0;top:215px;width:846px;height:425px;
  background:linear-gradient(180deg,#8fc3ea 0%,#cfe6f6 30%,#9fbf88 55%,#6f8a5a 75%,#e8ece6 100%)}
.merit{position:absolute;left:425px;top:430px;width:400px}
.merit-title{color:var(--white);font-size:26px;font-weight:700;letter-spacing:1px;border-bottom:1px solid var(--white);padding-bottom:2px;margin-bottom:8px}
.merit-title small{font-size:12px;font-weight:500;margin-left:10px}
.merit-row{display:flex;align-items:center;margin-bottom:7px}
.merit-tag{background:var(--red);color:var(--white);font-weight:700;font-size:17px;width:150px;text-align:center;padding:5px 0;flex:none}
.merit-note{color:var(--white);font-size:10px;line-height:1.4;margin-left:10px;text-shadow:0 0 3px rgba(0,0,0,.5)}
.plans{position:absolute;left:30px;top:655px;width:786px}
.plans-title{color:var(--navy);font-size:20px;font-weight:700;border-bottom:2px solid var(--blue);padding-bottom:4px}
.plan-list{display:flex;justify-content:space-between;margin-top:14px}
.plan{display:flex;align-items:center;gap:10px;width:255px}
.plan-name{border:2px solid var(--blue);border-radius:30px;color:var(--navy);font-size:19px;font-weight:700;padding:8px 14px;white-space:nowrap;line-height:1.2;text-align:center}
.plan-name small{display:block;font-size:10px;font-weight:500}
.fee{width:100px;height:100px;border-radius:50%;background:var(--yellow);display:flex;flex-direction:column;align-items:center;justify-content:center;flex:none}
.fee-label{font-size:11px;font-weight:700;color:var(--ink)}
.fee-sub{font-size:11px;color:var(--red);font-weight:700}
.fee-value{font-size:30px;color:var(--red);font-weight:900;line-height:1.05}
.footnote{position:absolute;left:30px;top:830px;width:786px;font-size:10px;color:var(--gray);line-height:1.5}
.contact{position:absolute;left:0;top:878px;width:846px;height:110px;background:var(--blue);color:var(--white);text-align:center}
.contact-label{font-size:14px;font-weight:500;padding-top:12px}
.contact-phone{display:flex;align-items:center;justify-content:center;gap:12px;font-size:50px;font-weight:900;line-height:1.2;letter-spacing:1px}
.contact-phone small{font-size:16px;font-weight:500}
.companies{position:absolute;left:30px;top:1010px;width:786px;display:flex;align-items:center;justify-content:space-between}
.company{width:350px;text-align:center}
.company-name{font-size:19px;font-weight:700;color:var(--navy);border-bottom:1px solid var(--navy);padding-bottom:4px;margin-bottom:5px}
.company-info{font-size:10px;color:var(--gray);line-height:1.5}
.cross{font-size:42px;color:var(--navy);font-weight:300}
</style>
</head>
<body>
<h1 class="headline">アパート・マンションの売却を<br>考えていらっしゃるオーナー様。<br>当社に買い取らせてください。</h1>
<p class="subline">入居者減少でお悩みの方も、ぜひ一度ご相談ください。</p>

<div class="photo" role="img" aria-label="青空と緑の木々に囲まれたマンションの前で、スーツ姿の担当者が手を差し出している写真"></div>

<section class="merit">
  <h2 class="merit-title">MERIT<small>当社の買取メリット</small></h2>
  <div class="merit-row"><span class="merit-tag">秘密厳守</span><p class="merit-note">お客様の情報は厳重に管理し、<br>外部に漏れることはありません。</p></div>
  <div class="merit-row"><span class="merit-tag">適正価格</span><p class="merit-note">市場調査に基づき、物件の価値を<br>適正に評価し査定いたします。</p></div>
  <div class="merit-row"><span class="merit-tag">実績豊富</span><p class="merit-note">地域密着で25年以上、入居率98%</p></div>
  <div class="merit-row"><span class="merit-tag">早期契約決済可</span><p class="merit-note">2週間以内の契約と決済が可能です</p></div>
</section>

<section class="plans">
  <h2 class="plans-title">管理は3タイプ揃えています。</h2>
  <div class="plan-list">
    <div class="plan">
      <span class="plan-name">①一般管理</span>
      <div class="fee"><span class="fee-label">管理料</span><span class="fee-sub">収納賃料の</span><span class="fee-value">3%</span></div>
    </div>
    <div class="plan">
      <span class="plan-name">②サブリース<small>家賃保証無し</small></span>
      <div class="fee"><span class="fee-label">管理料</span><span class="fee-sub">収納賃料の</span><span class="fee-value">5%</span></div>
    </div>
    <div class="plan">
      <span class="plan-name">③サブリース<small>社宅代行を<br>東和住まいリンク<br>が一括借上</small></span>
      <div class="fee"><span class="fee-label">管理料</span><span class="fee-sub">&nbsp;</span><span class="fee-value">無料</span></div>
    </div>
  </div>
</section>

<p class="footnote">※①②③は、空室の状況や物件の条件により異なります。ご契約内容の詳細は担当者までお気軽にお問い合わせください。<br>※管理料は税別です。サブリースの条件は物件ごとに審査のうえご案内いたします。</p>

<section class="contact">
  <p class="contact-label">ご相談・お問い合わせ</p>
  <p class="contact-phone">
    <svg width="40" height="40" viewBox="0 0 24 24" aria-hidden="true"><path fill="#f6e24c" d="M6.6 10.8a15 15 0 0 0 6.6 6.6l2.2-2.2c.3-.3.7-.4 1-.2 1.1.4 2.3.6 3.6.6.6 0 1 .4 1 1V20c0 .6-.4 1-1 1A17 17 0 0 1 3 4c0-.6.4-1 1-1h3.5c.6 0 1 .4 1 1 0 1.3.2 2.5.6 3.6.1.3 0 .7-.2 1z"/></svg>
    0575-26-8840<small>（カナメリビング株式会社）</small>
  </p>
</section>

<section class="companies">
  <div class="company">
    <p class="company-name">カナメリビング株式会社</p>
    <p class="company-info">〒501-3253 岐阜県関市桜台3丁目4-27<br>TEL 0575-38-4716<br>スミカネットFC岐阜北店・スミカネットFC各務原21号店・スミカネットFC関店</p>
  </div>
  <span class="cross">×</span>
  <div class="company">
    <p class="company-name">東和住まいリンク株式会社</p>
    <p class="company-info">〒500-8842 岐阜県岐阜市若葉町2丁目8-13<br>TEL 0575-24-5108<br>全国で社宅代行を受託・社宅として一括借上</p>
  </div>
</section>
</body>
</html>
```